Summer Drinks Flyer for Coffee Shop

We are a coffee shop in London and would like to have a cool and nice flyer for our summer drinks (juices and frozen drink) flyer - see on the attached file for the list

Attached you can find an "attempt" - please note that I would no necessary need the image below.

I also attache our new logo.

thank you

Industry/Entity Type

Coffee Shop

```html
<!DOCTYPE html>
<html lang="en">
<head>
<meta charset="utf-8">
<title>Summer Drinks Menu</title>
<link rel="stylesheet" href="https://fonts.googleapis.com/css2?family=Bebas+Neue&family=Montserrat:ital,wght@0,500;1,900&display=swap">
<style>
  :root {
    --sky: #3aa3d6;
    --mist: #c9dbe6;
    --slate: #3c3e40;
    --charcoal: #323436;
    --taupe: #8a7a66;
    --white: #ffffff;
    --lime: #76d11f;
    --tangerine: #ff7a1c;
  }
  * { margin: 0; padding: 0; box-sizing: border-box; }
  html, body { width: 838px; height: 1200px; overflow: hidden; }
  body { font-family: "Bebas Neue", sans-serif; color: var(--white); }

  .flyer {
    position: relative;
    width: 838px;
    height: 1200px;
    overflow: hidden;
    background:
      radial-gradient(ellipse 420px 520px at 838px 620px, rgba(170,140,105,.85), rgba(138,122,102,0) 70%),
      radial-gradient(ellipse 520px 380px at 560px 80px, rgba(230,240,245,.9), rgba(201,219,230,0) 70%),
      radial-gradient(ellipse 460px 360px at 838px 0, var(--sky), rgba(58,163,214,0) 80%),
      radial-gradient(ellipse 380px 300px at 420px 560px, rgba(120,160,185,.55), rgba(120,160,185,0) 75%),
      linear-gradient(180deg, #b9c6cd 0%, #6b7378 22%, var(--slate) 45%, var(--charcoal) 100%);
  }

  .section {
    position: absolute;
    transform: rotate(-4deg);
    transform-origin: 0 0;
  }
  .section--juices { left: 75px; top: 132px; width: 700px; }
  .section--coffees { left: 78px; top: 478px; width: 700px; }
  .section--frozen { left: 128px; top: 758px; width: 652px; }

  .section__title {
    font-family: "Montserrat", sans-serif;
    font-weight: 900;
    font-style: italic;
    font-size: 66px;
    line-height: .88;
    letter-spacing: -1px;
    text-transform: uppercase;
  }
  .section--coffees .section__title,
  .section--frozen .section__title { text-align: right; }

  .menu { list-style: none; }
  .section--juices .menu { margin-top: 8px; }
  .section--coffees .menu { margin-top: 26px; }
  .section--frozen .menu { margin-top: 20px; }

  .menu__item {
    display: flex;
    align-items: baseline;
    font-size: 37px;
    line-height: 42px;
    letter-spacing: .3px;
  }
  .menu__name { white-space: nowrap; }
  .menu__leader {
    flex: 1;
    border-bottom: 2px dotted var(--white);
    margin: 0 4px;
    transform: translateY(-6px);
  }
  .menu__price { white-space: nowrap; letter-spacing: 1px; }

  .note {
    font-family: "Montserrat", sans-serif;
    font-weight: 500;
    font-size: 14px;
    text-align: center;
    color: var(--white);
    height: 34px;
    line-height: 34px;
  }
  .note--lime { background: var(--lime); width: 772px; margin: 6px 0 0 -4px; }
  .note--tangerine { background: var(--tangerine); width: 780px; margin: 4px 0 0 -86px; padding-left: 86px; }

  .footer {
    position: absolute;
    left: 0; top: 1020px;
    width: 838px; height: 180px;
  }
  .footer svg { position: absolute; inset: 0; }
  .brand {
    position: absolute;
    left: 0; right: 0; top: 92px;
    text-align: center;
    font-family: "Bebas Neue", sans-serif;
    font-size: 50px;
    line-height: 1;
    letter-spacing: 6px;
    text-transform: uppercase;
    color: var(--charcoal);
  }
</style>
</head>
<body>
<main class="flyer">

  <section class="section section--juices">
    <h2 class="section__title">Fruit Juices</h2>
    <ul class="menu">
      <li class="menu__item"><span class="menu__name">Orange and Carrot</span><span class="menu__leader"></span><span class="menu__price">£ 2.95</span></li>
      <li class="menu__item"><span class="menu__name">Orange and Pineapple</span><span class="menu__leader"></span><span class="menu__price">£ 2.95</span></li>
      <li class="menu__item"><span class="menu__name">Pineapple and Apple</span><span class="menu__leader"></span><span class="menu__price">£ 2.95</span></li>
      <li class="menu__item"><span class="menu__name">Apple and Kiwi</span><span class="menu__leader"></span><span class="menu__price">£ 2.95</span></li>
      <li class="menu__item"><span class="menu__name">Carrot and Ginger</span><span class="menu__leader"></span><span class="menu__price">£ 2.95</span></li>
    </ul>
    <p class="note note--lime">add mint or ginger for free!</p>
  </section>

  <section class="section section--coffees">
    <h2 class="section__title">Iced Coffees</h2>
    <ul class="menu">
      <li class="menu__item"><span class="menu__name">Iced Coffee</span><span class="menu__leader"></span><span class="menu__price">£ 2.95</span></li>
      <li class="menu__item"><span class="menu__name">Iced Latte</span><span class="menu__leader"></span><span class="menu__price">£ 2.95</span></li>
      <li class="menu__item"><span class="menu__name">Iced Chocolate Drink</span><span class="menu__leader"></span><span class="menu__price">£ 2.95</span></li>
    </ul>
    <p class="note note--tangerine">add syrup shot for 10p</p>
  </section>

  <section class="section section--frozen">
    <h2 class="section__title">Frozen<br>Fruit Drinks</h2>
    <ul class="menu">
      <li class="menu__item"><span class="menu__name">Strawberry and Banana</span><span class="menu__leader"></span><span class="menu__price">£ 2.95</span></li>
      <li class="menu__item"><span class="menu__name">Pineapple, Mango and Banana</span><span class="menu__leader"></span><span class="menu__price">£ 2.95</span></li>
    </ul>
  </section>

  <footer class="footer">
    <svg width="838" height="180" viewBox="0 0 838 180" aria-hidden="true">
      <path d="M0 62 Q419 -8 838 62 L838 180 L0 180 Z" fill="#ffffff"/>
    </svg>
    <p class="brand">Zuccheria</p>
  </footer>

</main>
</body>
</html>
```